Publisher needs a book cover design for ‘Lanterns Over the Marsh Gate’ book

We need a book cover (front, back, spine) for the 2nd edition of a book entitled ‘Lanterns Over the Marsh Gate’ and subtitled ‘the quiet geography of tidal winds, ferry routes and harbour lanterns’ (inverted commas not to be part of the title and subtitle). The author is Rupert Calloway. The publisher is Vellmark Press. The finished size of the paperback version will be the industry standard 9" x 6". There will be paperback, hardback, and e-book versions. The final number of pages is expected to be in the region 150-180 pages. Text for the back cover is not yet available, but at the bottom of the back cover should be publisher logo (rectangular) on the left and space for the ISBN bar code on the right. The circular logo should be on the spine. The design should be original and not include any stock images that have been created by someone else or may require obtaining a copyright licence to use. Symbols in common use and not copyrighted are probably ok. There are no required images, photographs or symbols except the publisher logo at the left bottom of the back cover and lower spine. Spine lettering should be UK/US style with the top of the writing nearest the front cover. The designer is free to be creative using appropriate diagrams, symbols or abstract designs. Rectangular and circular variants of the publisher logo are attached. Designers are assured that when evaluating designs absolutely no notice whatsoever is taken of a designer's Pixo Rally ranking or status; We are completely output driven, so what matters is the design, not the ranking or status of the designer. In a similar way, designs are not evaluated as 'good' or 'bad' - the winning design will be chosen after review by a design review panel and is not decided arbitrarily by a single person. All submitted designs should be capable of effective copyright assignment.

Target Market(s)

Practitioners, parents, teachers, pupils and academics concerned with child protection, safeguarding and the elimination of emotional abuse of children in the classroom

Font styles to use
Serif
Sans Serif

Requirements
Must have
• • Title, author, edition, subtitle, publisher logo
Nice to have
• • Originality, innovation
Should not have
• • Stock images or anything else requiring additional copyright discussions and negotiations.

```html
<!DOCTYPE html>
<html lang="en">
<head>
<meta charset="utf-8">
<title>Lanterns Over the Marsh Gate – Cover Spread</title>
<link rel="stylesheet" href="https://fonts.googleapis.com/css2?family=Rubik+Dirt&family=Montserrat:wght@400;600&family=Libre+Baskerville&display=swap">
<style>
  :root {
    --ink: #050505;
    --scarlet: #f40a0a;
    --scarlet-deep: #d80606;
    --ring: #7a0a0c;
    --paper: #ffffff;
    --backdrop: #e2e2e2;
    --stamp-font: "Rubik Dirt", "Impact", sans-serif;
    --sans: "Montserrat", "Helvetica Neue", Arial, sans-serif;
    --serif: "Libre Baskerville", "Times New Roman", serif;
  }
  * { box-sizing: border-box; margin: 0; padding: 0; }
  html, body { width: 1200px; height: 800px; overflow: hidden; background: var(--backdrop); }

  .spread {
    position: absolute; left: 122px; top: 60px;
    width: 956px; height: 680px;
    color: var(--paper);
    box-shadow: 0 12px 30px rgba(0,0,0,.25);
  }
  .spread__ground { position: absolute; inset: 0; }

  .back-cover  { position: absolute; left: 0;     top: 0; width: 453px; height: 680px; }
  .spine       { position: absolute; left: 453px; top: 0; width: 50px;  height: 680px;
                 border-left: 1px solid rgba(0,0,0,.35); border-right: 1px solid rgba(0,0,0,.35);
                 display: flex; flex-direction: column; align-items: center;
                 padding: 24px 0 22px; }
  .front-cover { position: absolute; left: 503px; top: 0; width: 453px; height: 680px; }

  /* Back cover */
  .back-copy {
    position: absolute; left: 44px; top: 170px; width: 330px;
    font-family: var(--serif); font-size: 10.2px; line-height: 1.42;
    text-align: justify; hyphens: auto;
  }
  .back-copy h2 {
    font-family: var(--serif); font-weight: 400; font-size: 17px;
    margin: 16px 0 8px;
  }
  .imprint {
    position: absolute; left: 44px; top: 626px;
    display: flex; align-items: center; gap: 8px;
    font-family: var(--serif); font-size: 15px; letter-spacing: .06em;
    text-transform: uppercase;
  }
  .imprint__dot { width: 22px; height: 22px; border-radius: 50%; background: var(--paper); }

  /* Spine: stacked in flow so lines never collide */
  .spine__text {
    writing-mode: vertical-rl; white-space: nowrap; flex: none; line-height: 1;
  }
  .spine__edition { font-family: var(--sans); font-size: 10px; letter-spacing: .18em; }
  .spine__title   { margin-top: 34px; font-family: var(--stamp-font); font-size: 12.5px; letter-spacing: .03em; }
  .spine__author  { margin-top: 18px; font-family: var(--serif); font-size: 11px; letter-spacing: .08em; text-transform: uppercase; }
  .spine__imprint {
    margin-top: auto; flex: none;
    display: flex; flex-direction: column; align-items: center; gap: 4px;
    font-family: var(--serif); font-size: 7px; letter-spacing: .04em; text-transform: uppercase; text-align: center;
  }
  .spine__imprint-dot { width: 18px; height: 18px; border-radius: 50%; background: var(--paper); }

  /* Front cover */
  .edition {
    position: absolute; left: 0; right: 60px; top: 86px; text-align: center;
    font-family: var(--sans); font-size: 19px; letter-spacing: .16em;
  }
  .stamp-ring { position: absolute; left: 70px; top: 100px; width: 320px; height: 320px; }
  .title {
    position: absolute; left: 70px; top: 175px; width: 320px;
    font-family: var(--stamp-font); font-weight: 400; line-height: .98;
    text-align: center; text-transform: uppercase;
  }
  .title span { display: block; }
  .title__a { font-size: 38px; }
  .title__b { font-size: 34px; }
  .title__c { font-size: 54px; }
  .title__d { font-size: 54px; }
  .subtitle {
    position: absolute; left: 40px; width: 380px; top: 440px;
    font-family: var(--serif); font-size: 12.5px; line-height: 1.45;
    text-align: center; text-transform: uppercase; letter-spacing: .02em;
  }
  .author {
    position: absolute; left: 0; right: 0; top: 600px; text-align: center;
    font-family: var(--sans); font-size: 30px; letter-spacing: .08em; text-transform: uppercase;
  }
  .author strong { font-weight: 600; }
  .author span { font-weight: 400; }
</style>
</head>
<body>
  <main class="spread">
    <svg class="spread__ground" viewBox="0 0 956 680" width="956" height="680" aria-hidden="true">
      <rect width="956" height="680" fill="var(--ink)"/>
      <polygon fill="var(--scarlet)" points="
        0,118 22,122 40,112 60,114 78,100 98,104 118,98 138,92 160,96 178,84 200,88 222,94 244,82 266,88 288,78 312,84 334,94 356,86 380,78 400,90 420,84 440,98 453,108
        470,114 490,122 503,132
        520,130 540,126 560,112 580,116 600,100 620,92 640,96 660,84 680,70 700,74 720,62 740,66 760,54 780,58 800,46 820,50 840,40 860,44 880,32 900,36 920,26 940,30 956,22
        956,470 936,476 916,468 896,482 876,478 856,492 836,496 816,510 796,506 776,522 756,528 736,540 716,536 696,550 676,548 656,560 636,556 616,568 596,566 576,578 556,574 536,584 516,586 503,594
        490,596 470,598 453,588
        434,594 414,586 394,600 374,596 354,604 334,600 314,612 294,606 274,618 254,614 234,624 214,620 194,630 174,622 154,634 134,630 114,640 94,634 74,646 54,640 34,650 14,646 0,652" />
      <rect x="453" y="0" width="50" height="680" fill="var(--scarlet-deep)" opacity=".35"/>
    </svg>

    <section class="back-cover">
      <div class="back-copy">
        <p>We need a book cover (front, back, spine) for the 2nd edition of a book entitled ‘Lanterns Over the Marsh Gate’ and subtitled ‘the quiet geography of tidal winds, ferry routes and harbour lanterns’ (inverted commas not to be part of the title and subtitle). The author is Rupert Calloway. The publisher is Vellmark Press. The finished size of the paperback version will be the industry standard 9" x 6". There will be paperback, hardback, and e-book versions. The final number of pages is expected to be in the region 150-180 pages. Text for the back cover is not yet available, but at the bottom of the back cover should be publisher logo (rectangular) on the left and space for the ISBN bar code on the right. The circular logo should be on the spine.</p>
        <h2>Author Biography</h2>
        <p>Spine lettering should be UK/US style with the top of the writing nearest the front cover. The designer is free to be creative using appropriate diagrams, symbols or abstract designs. Rectangular and circular variants of the publisher logo are attached. Designers are assured that when evaluating designs absolutely no notice whatsoever is taken of a designer's Pixo Rally ranking or status; We are completely output driven, so what matters is the design, not the ranking or status of the designer.</p>
      </div>
      <div class="imprint"><span class="imprint__dot"></span>Vellmark Press</div>
    </section>

    <section class="spine">
      <div class="spine__text spine__edition">2ND EDITION</div>
      <div class="spine__text spine__title">LANTERNS OVER THE MARSH GATE</div>
      <div class="spine__text spine__author">Rupert Calloway</div>
      <div class="spine__imprint"><span class="spine__imprint-dot"></span>Vellmark</div>
    </section>

    <section class="front-cover">
      <p class="edition">2ND EDITION</p>
      <svg class="stamp-ring" viewBox="0 0 320 320" aria-hidden="true">
        <circle cx="160" cy="160" r="128" fill="none" stroke="var(--ring)" stroke-width="22" opacity=".9"/>
        <circle cx="22" cy="58" r="11" fill="var(--ring)"/>
      </svg>
      <h1 class="title">
        <span class="title__a">Lanterns</span>
        <span class="title__b">Over the</span>
        <span class="title__c">Marsh</span>
        <span class="title__d">Gate</span>
      </h1>
      <p class="subtitle">The quiet geography of tidal winds,<br>ferry routes and harbour lanterns</p>
      <p class="author"><strong>Rupert</strong> <span>Calloway</span></p>
    </section>
  </main>
</body>
</html>
```